Kestrel Summit 2019 Enemies of the End-Times Church Flyer

We want a church conference flyer designed. We are looking for a professional, yet catchy design that uses our brand colors and logo creatively while communicating key information of the event effectively. <br/>The flyer must include all of the following:<br/>Title: Kestrel Summit 2019<br/>Topic: The Enemies of The End-Times Church <br/>Subtitles: <br/> -How the antichrist raises an army by social behavior engineering. <br/>-How the architects of modern social constructs escaped the church's radar. <br/>-The Holy Spirit's end-times agenda:<br/> The Knock-Out Punch!<br/>Speaker: Prophet Marcus Toliver <br/>Dates/time: December 27, 28 & 29 at 6pm<br/>Location: Halvorn Community Center <br/> 241 Pellham Street <br/> Portland, ME 04102<br/>Contact info: phone: 207-555-0148 <br/>email: contact@brookmeadow.example <br/> www.vutel.example<br/>*The flyer must also include a picture of the speaker and our Vutel logo <br/>Thanks, we look forward to seeing what you come up with!

Colors

Designer to choose colors to be used in the design.

Requirements
Must have
• The flyer must include all of the following:
• Title: Kestrel Summit 2019
• Topic: The Enemies of The End-Times Church
• Subtitles:
• -How the antichrist raises an army by social behavior engineering.
• -How the architects of modern social constructs escaped the church's radar.
• -The Holy Spirit's end-times agenda:
• The Knock-Out Punch!
• Speaker: Prophet Marcus Toliver
• Dates/time: December 27, 28 & 29 at 6pm
• Location: Halvorn Community Center
• 241 Pellham Street
• Portland, ME 04102
• Contact info: phone: 207-555-0148
• email: contact@brookmeadow.example
• www.vutel.example
• *The flyer must also include a picture of the speaker and our Vutel logo
Should not have
• Pictures of crosses or church buildings

```html
<!DOCTYPE html>
<html lang="en">
<head>
<meta charset="utf-8">
<title>Kestrel Summit 2019 – The Enemies of the End-Times Church</title>
<link rel="stylesheet" href="https://fonts.googleapis.com/css2?family=Cinzel:wght@400;600;700&family=Oswald:wght@400;500;600&family=Open+Sans:wght@400;600;700&display=swap">
<style>
  :root {
    --teal-deep: #0c2230;
    --teal-mid: #1d4656;
    --orange: #f39a2b;
    --peach: #f7b98a;
    --white: #ffffff;
    --navy: #0f2a47;
  }
  * { margin: 0; padding: 0; box-sizing: border-box; }
  html, body { width: 778px; height: 1200px; overflow: hidden; background: var(--teal-deep); }
  .flyer {
    position: relative; width: 778px; height: 1200px; overflow: hidden;
    font-family: "Open Sans", sans-serif; color: var(--white);
  }
  .backdrop {
    position: absolute; inset: 0 0 220px 0;
    background:
      radial-gradient(ellipse at 75% 20%, rgba(120,170,185,.45), transparent 55%),
      radial-gradient(ellipse at 20% 60%, rgba(60,110,130,.35), transparent 60%),
      linear-gradient(160deg, var(--teal-mid) 0%, var(--teal-deep) 70%);
  }
  .event-name { position: absolute; left: 165px; top: 32px; }
  .event-name .word {
    display: block; font-family: "Cinzel", serif; color: var(--orange);
    font-weight: 700; line-height: 1;
  }
  .event-name .word-1 { font-size: 32px; letter-spacing: 1px; }
  .event-name .word-2 { font-size: 24px; letter-spacing: 1px; margin-top: 6px; }
  .event-year {
    position: absolute; left: 370px; top: 22px;
    font-family: "Cinzel", serif; font-weight: 700; font-size: 84px; color: var(--orange); line-height: 1;
  }
  .topic-box {
    position: absolute; left: 92px; top: 180px; width: 666px; height: 206px;
    border: 2px solid var(--white); text-align: center; padding-top: 22px;
  }
  .topic-box .line-big { font-family: "Cinzel", serif; font-size: 72px; font-weight: 600; line-height: 1; letter-spacing: 1px; }
  .topic-box .line-small { font-family: "Cinzel", serif; font-size: 22px; font-weight: 600; margin: 6px 0 4px; }
  .topic-box .line-mid { font-family: "Cinzel", serif; font-size: 50px; font-weight: 600; line-height: 1; }
  .sessions { position: absolute; left: 96px; top: 445px; width: 600px; list-style: none; }
  .session {
    font-family: "Oswald", sans-serif; font-weight: 500; font-size: 21px; line-height: 1.27;
    color: var(--peach); text-transform: uppercase; margin-bottom: 22px;
  }
  .session::after {
    content: ""; display: block; width: 70px; height: 3px; background: var(--orange); margin-top: 12px;
  }
  .details { position: absolute; left: 40px; top: 765px; }
  .detail-row { display: flex; align-items: flex-start; gap: 14px; font-size: 23px; text-transform: uppercase; line-height: 1.3; }
  .detail-row strong { font-weight: 700; }
  .when { display: flex; gap: 60px; }
  .where { margin-top: 42px; text-transform: none; line-height: 1.3; }
  .where strong { color: var(--orange); }
  .icon { width: 28px; height: 28px; flex: none; margin-top: 2px; }
  .speaker-photo {
    position: absolute; left: 518px; top: 680px; width: 196px; height: 190px;
    background: linear-gradient(180deg, #6b7f8c 0%, #3a4a56 55%, #8a2b2b 100%);
  }
  .speaker { position: absolute; left: 518px; top: 896px; }
  .speaker .role { font-size: 20px; }
  .speaker .role strong { color: var(--orange); font-weight: 700; }
  .speaker .name { font-size: 30px; font-weight: 700; line-height: 1.2; color: var(--orange); }
  .footer {
    position: absolute; left: 0; right: 0; bottom: 0; height: 220px; background: var(--navy);
    display: flex; align-items: center;
  }
  .brand { width: 390px; padding-left: 44px; }
  .brand-mark { display: flex; align-items: center; gap: 16px; }
  .brand-dot { width: 34px; height: 34px; border-radius: 50%; background: var(--orange); }
  .brand-name { font-family: "Cinzel", serif; font-weight: 700; font-size: 70px; color: var(--white); line-height: 1; }
  .divider { width: 2px; height: 130px; background: var(--white); }
  .contact { padding-left: 36px; }
  .contact .phone { font-family: "Open Sans", sans-serif; font-size: 40px; font-weight: 700; line-height: 1.15; }
  .contact .email { font-size: 20px; line-height: 1.5; }
  .contact .web { font-size: 28px; font-weight: 700; line-height: 1.3; }
</style>
</head>
<body>
<div class="flyer">
  <div class="backdrop" role="img" aria-label="Dark teal abstract atmospheric background with soft light streaks"></div>

  <div class="event-name"><span class="word word-1">KESTREL</span><span class="word word-2">SUMMIT</span></div>
  <div class="event-year">2019</div>

  <div class="topic-box">
    <div class="line-big">THE ENEMIES</div>
    <div class="line-small">OF THE</div>
    <div class="line-mid">END-TIMES CHURCH</div>
  </div>

  <ul class="sessions">
    <li class="session">How the antichrist raises an army by social behavior engineering</li>
    <li class="session">How the architects of modern social constructs escaped the church’s radar</li>
    <li class="session">The Holy Spirit’s end-times agenda:<br>the knock-out punch!</li>
  </ul>

  <div class="details">
    <div class="when">
      <div class="detail-row">
        <svg class="icon" viewBox="0 0 24 24" fill="none" stroke="#f39a2b" stroke-width="2"><rect x="3" y="5" width="18" height="16" rx="2"/><path d="M3 10h18M8 3v4M16 3v4"/><path d="M7 14h2M11 14h2M15 14h2M7 17h2M11 17h2" stroke-width="1.6"/></svg>
        <span>December<br><strong>27, 28 &amp; 29</strong></span>
      </div>
      <div class="detail-row">
        <svg class="icon" viewBox="0 0 24 24" fill="none" stroke="#f39a2b" stroke-width="2"><circle cx="12" cy="12" r="9"/><path d="M12 7v5l3 2"/></svg>
        <strong>6PM</strong>
      </div>
    </div>
    <div class="detail-row where">
      <svg class="icon" viewBox="0 0 24 24" fill="none" stroke="#f39a2b" stroke-width="2"><path d="M12 22s7-7.5 7-13a7 7 0 0 0-14 0c0 5.5 7 13 7 13z"/><circle cx="12" cy="9" r="2.5"/></svg>
      <span><strong>Halvorn Community Center</strong><br>241 Pellham Street<br>Portland, ME 04102</span>
    </div>
  </div>

  <div class="speaker-photo" role="img" aria-label="Portrait photo of speaker Prophet Marcus Toliver in a dark suit"></div>
  <div class="speaker">
    <div class="role">Speaker: <strong>Prophet</strong></div>
    <div class="name">Marcus Toliver</div>
  </div>

  <footer class="footer">
    <div class="brand">
      <div class="brand-mark"><span class="brand-dot"></span><span class="brand-name">VUTEL</span></div>
    </div>
    <div class="divider"></div>
    <div class="contact">
      <div class="phone">207-555-0148</div>
      <div class="email">contact@brookmeadow.example</div>
      <div class="web">www.vutel.example</div>
    </div>
  </footer>
</div>
</body>
</html>
```